International Legal Service Company needs Letterhead Design

Put my new Logo into Letterhead Design, using updated telephone number, e-mail address and website. Current letterhead and updated information which i want you to include my new letterhead attached herewith. Of course, my new Logo attached herein. Also, you can use slogan "Total Legal Outsourcing Solutions For Multinational Businesses"

It Company

```html
<!DOCTYPE html>
<html lang="en">
<head>
<meta charset="utf-8">
<title>Meridian Counsel Partners Inc – Letterhead</title>
<link rel="stylesheet" href="https://fonts.googleapis.com/css2?family=Jost:wght@400;500;600&display=swap">
<style>
  :root {
    --backdrop: #2b2c2b;
    --paper: #ffffff;
    --brand-blue: #1d3f7c;
    --band-blue: #1b5e9e;
    --icon-blue: #2a5b9a;
    --ink: #1c1c1c;
    --rule: #3d6fae;
  }
  html, body {
    margin: 0;
    padding: 0;
    width: 1200px;
    height: 1000px;
    overflow: hidden;
    background: var(--backdrop);
    font-family: "Jost", sans-serif;
  }
  .letterhead {
    position: absolute;
    left: 294px;
    top: 104px;
    width: 612px;
    height: 792px;
    background: var(--paper);
    overflow: hidden;
  }
  .brand {
    position: absolute;
    left: 33px;
    top: 22px;
    display: flex;
    align-items: center;
    gap: 10px;
  }
  .brand-dot {
    width: 56px;
    height: 56px;
    border-radius: 50%;
    background: var(--brand-blue);
  }
  .brand-name {
    color: var(--brand-blue);
    font-weight: 600;
    font-size: 17px;
    line-height: 19px;
  }
  .slogan {
    position: absolute;
    right: 192px;
    top: 44px;
    text-align: right;
    color: var(--brand-blue);
    font-size: 7.6px;
    line-height: 10px;
    letter-spacing: 0.2px;
    text-transform: uppercase;
  }
  .contact-rule {
    position: absolute;
    left: 430px;
    top: 20px;
    width: 1px;
    height: 69px;
    background: var(--rule);
  }
  .contact-list {
    position: absolute;
    left: 438px;
    top: 17px;
    margin: 0;
    padding: 0;
    list-style: none;
    font-size: 9.6px;
    line-height: 12.5px;
    color: var(--ink);
  }
  .contact-list li {
    display: flex;
    align-items: flex-start;
    gap: 4px;
  }
  .contact-icon {
    flex: none;
    width: 6px;
    height: 6px;
    margin-top: 3px;
    border-radius: 1px;
    background: var(--icon-blue);
  }
  .contact-address span { display: block; }
  .contact-address span + span { margin-left: -6px; }
  .footer-band {
    position: absolute;
    left: 0;
    bottom: 0;
    width: 612px;
    height: 19px;
  }
</style>
</head>
<body>
  <main class="letterhead">
    <header>
      <div class="brand">
        <div class="brand-dot" aria-hidden="true"></div>
        <div class="brand-name">Meridian Counsel<br>Partners Inc</div>
      </div>
      <p class="slogan">Total legal outsourcing solutions<br>for multinational businesses</p>
      <div class="contact-rule" aria-hidden="true"></div>
      <ul class="contact-list">
        <li><span class="contact-icon"></span>240-555-0147</li>
        <li><span class="contact-icon"></span>240-555-0188</li>
        <li><span class="contact-icon"></span>office@meridiancounsel.com</li>
        <li><span class="contact-icon"></span>http://meridiancounsel.net</li>
        <li class="contact-address"><span class="contact-icon"></span><div><span>4120 Harbor Point Drive</span><span>Suite 300, Lakeside, MD 20999</span></div></li>
      </ul>
    </header>
    <svg class="footer-band" viewBox="0 0 612 19" aria-hidden="true">
      <rect width="612" height="19" fill="var(--band-blue)"/>
      <polygon points="444,0 458,0 452,19 438,19" fill="#ffffff"/>
      <polygon points="444,0 450,0 444,19 438,19" fill="#111111"/>
    </svg>
  </main>
</body>
</html>
```